Lanternfield Drinks business cards

We need a business card design for our new logo. The company is modern, progressive, professional, yet approachable. The key products are ready to drink bottles and cans of coffee based beverages.
These cards will be a critical part of the first impression made by our sales organization, business development team, and all external facing personnel.
Card can be a vertical or horizontal orientation.

Target Market(s)

Customers, suppliers, business partners

Industry/Entity Type

Business

Contact Information for Business Card

Business cards should feature Company Name and Logo.

Font styles to use
Serif

Colors

Designer to choose colors to be used in the design.

Requirements
Must have
• Strong readability of Name, phone #, mobile number and email address.
• Job title, website url, Street Address, and other details can be secondary level readability.
Nice to have
• High impact, simplistic quality design.
• Ok to utilize the 'H in the box' separate from the company name

```html
<!DOCTYPE html>
<html lang="en">
<head>
<meta charset="utf-8">
<title>Lanternfield Drinks – Business Cards</title>
<link rel="stylesheet" href="https://fonts.googleapis.com/css2?family=Cinzel:wght@600;700&family=Open+Sans:wght@400&family=Roboto+Slab:wght@400;600&display=swap">
<style>
  :root {
    --backdrop: #1b1b1c;
    --card-dark: #221a1a;
    --card-dark-edge: #2e2524;
    --orange: #f0643c;
    --orange-deep: #e8572f;
    --orange-soft: #f58a54;
    --amber: #f6a52a;
    --yellow: #f7bd2c;
    --white: #ffffff;
    --text-light: #f2efee;
  }
  * { box-sizing: border-box; margin: 0; padding: 0; }
  html, body { width: 1200px; height: 864px; overflow: hidden; }
  body { background: var(--backdrop); position: relative; }

  .card {
    position: absolute;
    width: 520px;
    height: 300px;
    overflow: hidden;
    border-radius: 3px;
  }

  /* Front */
  .card--front {
    left: 560px; top: 110px;
    background: linear-gradient(160deg, var(--orange) 0%, var(--orange-deep) 55%, #e0704e 100%);
  }
  .front-tile { position: absolute; }
  .front-tile--amber { left: 330px; top: 0; width: 110px; height: 135px; background: var(--amber); }
  .front-tile--orange { left: 440px; top: 135px; width: 80px; height: 90px; background: var(--orange-deep); }
  .front-tile--white { left: 230px; top: 135px; width: 210px; height: 165px; background: var(--white); }
  .front-tile--white-right { left: 440px; top: 225px; width: 80px; height: 75px; background: var(--white); }
  .front-tile--mark {
    left: 270px; top: 165px; width: 140px; height: 110px;
    background: var(--orange);
    display: flex; align-items: center; justify-content: center;
  }
  .wordmark {
    position: absolute; left: 28px; top: 92px;
    font-family: "Roboto Slab", serif; font-weight: 600;
    font-size: 30px; letter-spacing: 1px; color: var(--white);
    text-transform: uppercase; line-height: 1.1;
  }
  .wordmark-rule {
    position: absolute; left: 28px; top: 136px;
    width: 180px; height: 1px; background: var(--amber);
  }
  .mark-name {
    font-family: "Roboto Slab", serif; font-weight: 600;
    font-size: 17px; color: var(--white); text-align: center; line-height: 1.2;
  }

  /* Back */
  .card--back {
    left: 120px; top: 470px;
    background: linear-gradient(150deg, var(--card-dark) 0%, var(--card-dark) 60%, var(--card-dark-edge) 100%);
  }
  .back-band { position: absolute; }
  .back-band--yellow { left: 105px; top: 0; width: 120px; height: 300px; background: linear-gradient(180deg, var(--yellow), var(--amber)); }
  .back-band--orange { left: 0; top: 70px; width: 225px; height: 140px; background: linear-gradient(90deg, var(--orange-deep), var(--orange-soft)); }
  .back-band--white {
    left: 105px; top: 70px; width: 120px; height: 140px; background: var(--white);
    display: flex; align-items: center; justify-content: center;
  }
  .back-mark {
    font-family: "Roboto Slab", serif; font-weight: 600;
    font-size: 14px; color: var(--orange); text-align: center; line-height: 1.25;
  }

  .contact { position: absolute; left: 262px; top: 68px; color: var(--text-light); }
  .contact-name {
    font-family: "Cinzel", serif; font-weight: 700;
    font-size: 15px; color: var(--orange); letter-spacing: 0.5px;
  }
  .contact-title {
    font-family: "Open Sans", sans-serif; font-size: 11.5px; margin-top: 1px;
  }
  .contact-address {
    font-family: "Roboto Slab", serif; font-size: 11px; color: var(--amber);
    margin-top: 10px; line-height: 1.35;
  }
  .contact-lines { list-style: none; margin-top: 14px; }
  .contact-line {
    display: flex; align-items: center; gap: 10px;
    font-family: "Roboto Slab", serif; font-size: 11.5px; line-height: 1.55;
  }
  .contact-icon { width: 11px; height: 11px; flex: none; }
</style>
</head>
<body>

<section class="card card--front" aria-label="Card front">
  <div class="front-tile front-tile--amber"></div>
  <div class="front-tile front-tile--orange"></div>
  <div class="front-tile front-tile--white"></div>
  <div class="front-tile front-tile--white-right"></div>
  <div class="front-tile front-tile--mark"><span class="mark-name">Lanternfield<br>Drinks</span></div>
  <h1 class="wordmark">Lanternfield<br>Drinks</h1>
</section>

<section class="card card--back" aria-label="Card back">
  <div class="back-band back-band--yellow"></div>
  <div class="back-band back-band--orange"></div>
  <div class="back-band back-band--white"><span class="back-mark">Lanternfield<br>Drinks</span></div>

  <div class="contact">
    <h2 class="contact-name">DANIEL WHITCOMBE</h2>
    <p class="contact-title">Managing Director</p>
    <p class="contact-address">418 Harbor View Rd.<br>Millbrook, NY 11590</p>
    <ul class="contact-lines">
      <li class="contact-line">
        <svg class="contact-icon" viewBox="0 0 12 12"><rect x="0.5" y="0.5" width="11" height="11" fill="none" stroke="#f0643c"/><path d="M3.5 3 L5 3 L5.5 4.5 L4.7 5.2 Q5.6 6.8 6.8 7.3 L7.5 6.5 L9 7 L9 8.5 Q5 9 3.5 3Z" fill="#f0643c"/></svg>
        555.301.4420
      </li>
      <li class="contact-line">
        <svg class="contact-icon" viewBox="0 0 12 12"><rect x="0.5" y="0.5" width="11" height="11" fill="none" stroke="#f0643c"/><rect x="4" y="2.5" width="4" height="7" rx="0.6" fill="none" stroke="#f0643c"/></svg>
        555.208.7731
      </li>
      <li class="contact-line">
        <svg class="contact-icon" viewBox="0 0 12 12"><rect x="0.5" y="0.5" width="11" height="11" fill="none" stroke="#f0643c"/><rect x="2.5" y="3.5" width="7" height="5" fill="none" stroke="#f0643c"/><path d="M2.5 3.5 L6 6.5 L9.5 3.5" fill="none" stroke="#f0643c"/></svg>
        dan@lanternfielddrinks.com
      </li>
      <li class="contact-line">
        <svg class="contact-icon" viewBox="0 0 12 12"><rect x="0.5" y="0.5" width="11" height="11" fill="none" stroke="#f0643c"/><circle cx="6" cy="6" r="3.2" fill="none" stroke="#f0643c"/><path d="M2.8 6 H9.2 M6 2.8 V9.2" stroke="#f0643c"/></svg>
        www.lanternfielddrinks.com
      </li>
    </ul>
  </div>
</section>

</body>
</html>
```